Canvasline Registry, LLC needs clean, modern business card design

Canvasline Registry is based in Honolulu. We offer fine arts collections management and documentation services for private and corporate art collectors. I would like to use my logo (attached). Card can be either single or double sided and either vertical or horizontal. My clients are businesses with art collections (banks, law firms, etc.) and wealthy individual collectors.

```html
<!DOCTYPE html>
<html lang="en">
<head>
<meta charset="utf-8">
<title>Canvasline Registry business card</title>
<link href="https://fonts.googleapis.com/css2?family=Lato:wght@400;700&display=swap" rel="stylesheet">
<style>
  :root {
    --backdrop: #3b3431;
    --card: #1b1b1c;
    --card-edge: #2a2a2b;
    --accent: #38a9e1;
    --ink: #f1f1f1;
    --ink-soft: #c9c9c9;
    --mark: #dfe6ee;
    --mark-ring: #9aa4ae;
    --rule: #3a3a3c;
  }
  * { box-sizing: border-box; margin: 0; padding: 0; }
  html, body { width: 1200px; height: 844px; overflow: hidden; }
  body {
    background: var(--backdrop);
    font-family: "Lato", Arial, sans-serif;
    position: relative;
  }
  .card {
    position: absolute;
    top: 268px;
    width: 540px;
    height: 309px;
    background: radial-gradient(ellipse at 60% 40%, #232324 0%, var(--card) 70%);
    border: 1px solid var(--card-edge);
    box-shadow: 0 14px 30px rgba(0,0,0,.45);
  }
  .card--front { left: 40px; }
  .card--back { left: 620px; }

  .front-mark {
    position: absolute;
    left: 62px;
    top: 92px;
    width: 160px;
    text-align: center;
  }
  .mark-circle {
    display: block;
    width: 96px;
    height: 96px;
    margin: 0 auto 12px;
    border-radius: 50%;
    background: var(--mark);
    border: 4px solid var(--mark-ring);
  }
  .front-mark .brand-name {
    font-size: 14px;
    color: var(--ink);
    letter-spacing: .5px;
  }
  .divider {
    position: absolute;
    left: 262px;
    top: 70px;
    width: 1px;
    height: 170px;
    background: var(--rule);
  }
  .contact {
    position: absolute;
    left: 282px;
    top: 74px;
    color: var(--ink);
    font-size: 14px;
    line-height: 1.3;
  }
  .contact .person { font-size: 21px; color: var(--accent); line-height: 1.1; }
  .contact .role { margin-bottom: 14px; }
  .contact .address { margin-bottom: 14px; }
  .contact .label { color: var(--accent); display: inline-block; width: 16px; }

  .back-logo {
    position: absolute;
    left: 0; right: 0; top: 0; bottom: 0;
    display: flex;
    align-items: center;
    justify-content: center;
    gap: 16px;
  }
  .back-logo .brand-name {
    font-size: 34px;
    color: var(--ink-soft);
  }
  .back-logo .mark-circle {
    width: 70px;
    height: 70px;
    margin: 0;
    border-width: 3px;
  }
</style>
</head>
<body>
  <section class="card card--front" aria-label="Card front">
    <div class="front-mark">
      <span class="mark-circle" aria-hidden="true"></span>
      <span class="brand-name">Canvasline Registry</span>
    </div>
    <div class="divider"></div>
    <div class="contact">
      <p class="person">Malia Kahananui</p>
      <p class="role">Managing Director</p>
      <p class="address">1450, Kapiolani Blvd<br>Honolulu, HI 96814.</p>
      <p><span class="label">T:</span> 808-555 0142</p>
      <p><span class="label">E:</span> info@canvasline.com</p>
      <p><span class="label">W:</span>www.canvaslinereg.com</p>
    </div>
  </section>

  <section class="card card--back" aria-label="Card back">
    <div class="back-logo">
      <span class="brand-name">Canvasline Registry</span>
      <span class="mark-circle" aria-hidden="true"></span>
    </div>
  </section>
</body>
</html>
```